BrightHaven Cleaning Services - inviting website needed to gain residential and commercial clients

Hello! I need a website for a newly created company that specializes in residential and commercial cleaning services. We clean homes, apartments, condos, rental apt for people that are too busy or don't want to spend time cleaning when they can be doing other things - whether that's because of long working hours or a business family schedule or perhaps for seniors that find it challenging to clean their homes.
In addition, for businesses we offer cleaning services of offices, doctors/dentist offices, essentially any business.
The BrightHaven Cleaning Services is BrightHaven Cleaning Services which means we offer cleaning services not just inside homes and business but also outside. The outside services we offer include lawn mowing, pressure washing and snow removal.
I'm looking for a clean, contemporary design.
We are environmentally continuous and therefore use products that are not harmful to the environment, people or pets.
I should also mention that I would like to offer booking pages on the site as well so that clients can schedule their cleans and pay on line via credit card.
Website copy to be provided shortly but am hoping to see the initial design concept first?? Or if it helps, I can send copy in a few days

```html
<!DOCTYPE html>
<html lang="en">
<head>
<meta charset="utf-8">
<title>BrightHaven Cleaning Services</title>
<link href="https://fonts.googleapis.com/css2?family=Montserrat:wght@400;500;600&family=Mulish:wght@400;600;700&display=swap" rel="stylesheet">
<style>
:root{
  --blue:#1a8fd6;
  --blue-deep:#1b67c4;
  --navy:#1f2e8e;
  --navy-dark:#16236d;
  --green:#4aa832;
  --green-dark:#0f6b32;
  --ink:#222;
  --text:#555;
  --grey-band:#e6e6e6;
  --white:#fff;
}
*{margin:0;padding:0;box-sizing:border-box}
html,body{width:1200px;height:2885px;overflow:hidden;background:var(--white)}
body{position:relative;font-family:'Mulish',sans-serif;color:var(--ink)}
.abs{position:absolute}

/* header */
.site-header{position:absolute;left:0;top:0;width:1200px;height:112px;background:var(--white);z-index:5;box-shadow:0 2px 6px rgba(0,0,0,.12)}
.brand-badge{position:absolute;left:118px;top:0;width:196px;height:156px;background:var(--white);border-radius:0 0 98px 98px;z-index:6;display:flex;flex-direction:column;align-items:center;justify-content:center;gap:8px}
.brand-dot{width:34px;height:34px;border-radius:50%;background:var(--blue-deep)}
.brand-name{font-family:'Mulish',sans-serif;font-weight:700;font-size:15px;color:var(--navy);text-align:center;line-height:1.2;width:170px}
.header-phone{position:absolute;left:904px;top:20px;font-family:'Mulish',sans-serif;font-size:19px;color:var(--blue-deep);display:flex;align-items:center;gap:6px}
.main-nav{position:absolute;top:66px;left:0;width:1200px;font-family:'Mulish',sans-serif;font-size:16.5px;color:#333}
.main-nav a{position:absolute;color:inherit;text-decoration:none;white-space:nowrap}
.main-nav a.active{color:var(--blue)}

/* hero */
.hero{position:absolute;left:0;top:112px;width:1200px;height:640px;overflow:hidden;
  background:linear-gradient(180deg,#3f86d8 0%,#7fb3e8 45%,#d9e3ec 68%,#c9c1a8 100%)}
.hero-photo{position:absolute;inset:0;background:radial-gradient(ellipse 360px 300px at 900px 300px,rgba(232,178,30,.9),rgba(232,178,30,0) 70%),radial-gradient(ellipse 250px 200px at 90px 480px,rgba(255,255,255,.9),rgba(255,255,255,0) 70%)}
.hero-blob{position:absolute;left:96px;top:100px}
.hero-title{position:absolute;left:150px;top:206px;width:390px;text-align:center;color:var(--white);font-family:'Montserrat',sans-serif}
.hero-title h1{font-size:38px;font-weight:500;letter-spacing:.5px}
.hero-title p{font-size:27px;font-weight:400;margin-top:2px}
.btn-outline{position:absolute;border:2px solid var(--white);border-radius:22px;color:var(--white);font-family:'Mulish',sans-serif;font-weight:700;font-size:16px;display:flex;align-items:center;justify-content:center}
.hero-call{left:271px;top:290px;width:148px;height:42px}
.hero-curve{position:absolute;left:0;top:538px}
.dot{position:absolute;width:13px;height:13px;border-radius:50%;background:var(--white)}
.dot.ring{background:transparent;border:2px solid var(--white)}

/* section headings */
.section-title{position:absolute;left:0;width:1200px;text-align:center;font-family:'Montserrat',sans-serif;font-weight:500;font-size:32px;color:var(--ink)}
.divider{position:absolute;left:423px;width:346px;height:24px}

/* services */
.service-card{position:absolute;top:806px;width:306px;height:286px;overflow:hidden}
.service-photo{position:absolute;left:0;top:0;width:306px;height:286px}
.service-label{position:absolute;left:0;top:207px;width:306px;height:56px;color:var(--white);font-family:'Montserrat',sans-serif;font-size:21px;display:flex;align-items:center;justify-content:center}

/* about */
.about{position:absolute;left:0;top:1158px;width:1200px;height:478px;overflow:hidden;background:linear-gradient(180deg,#7fae58 0%,#5f9e2f 40%,#3e7f1e 100%)}
.about-panel{position:absolute;left:0;top:0}
.about-copy{position:absolute;left:733px;top:110px;width:370px;color:var(--white)}
.about-copy h2{font-family:'Montserrat',sans-serif;font-weight:500;font-size:31px;line-height:1.08}
.about-copy p{font-size:15px;line-height:1.55;margin-top:18px;color:#eaf6e2}
.about-copy p + p{margin-top:14px}
.about-more{left:733px;top:1491px;width:154px;height:44px;position:absolute}

/* recent work */
.work{position:absolute;left:0;top:1636px;width:1200px;height:451px;background:var(--grey-band)}
.work-photo{position:absolute;top:131px;width:258px;height:258px;border-radius:50%;box-shadow:0 4px 10px rgba(0,0,0,.25)}

/* why us */
.why{position:absolute;left:0;top:2087px;width:1200px;height:457px;overflow:hidden;background:var(--white)}
.why-photo{position:absolute;left:420px;top:0;width:780px;height:457px;background:linear-gradient(90deg,rgba(255,255,255,1) 0%,rgba(255,255,255,.6) 30%,rgba(255,255,255,0) 65%),linear-gradient(160deg,#f4f0ea 0%,#e7dccb 45%,#3f9a42 75%,#e9c33a 100%)}
.why-copy{position:absolute;left:154px;top:66px;width:470px}
.why-copy h2{font-family:'Montserrat',sans-serif;font-weight:500;font-size:32px;color:var(--ink)}
.why-copy p{font-size:15px;line-height:1.55;color:var(--text);margin-top:18px}
.why-copy p + p{margin-top:14px}
.btn-solid{position:absolute;left:146px;top:2385px;width:152px;height:42px;border-radius:22px;background:var(--blue);color:var(--white);font-weight:700;font-size:16px;display:flex;align-items:center;justify-content:center}

/* footer */
.site-footer{position:absolute;left:0;top:2544px;width:1200px;height:283px;background:var(--navy);color:var(--white)}
.footer-brand{position:absolute;left:150px;top:70px;width:190px;display:flex;flex-direction:column;align-items:center;gap:10px}
.footer-brand .brand-dot{background:var(--white)}
.footer-brand .brand-name{color:var(--white);font-size:16px}
.footer-col{position:absolute;top:63px}
.footer-col h3{font-family:'Montserrat',sans-serif;font-weight:500;font-size:17px;letter-spacing:.3px}
.footer-col ul{list-style:none;margin-top:18px}
.footer-col li{font-size:15px;line-height:30.5px;color:#e6e9ff}
.contact-line{display:flex;gap:10px;align-items:flex-start}
.copyright{position:absolute;left:0;top:2827px;width:1200px;height:58px;background:var(--navy-dark);color:#9aa4d8;font-size:13px;display:flex;align-items:center;justify-content:center}
</style>
</head>
<body>

<header class="site-header">
  <div class="header-phone">
    <svg width="18" height="18" viewBox="0 0 24 24"><path d="M6.6 10.8a15.5 15.5 0 0 0 6.6 6.6l2.2-2.2c.3-.3.7-.4 1-.2 1.1.4 2.3.6 3.6.6.6 0 1 .4 1 1V20c0 .6-.4 1-1 1C10.6 21 3 13.4 3 4c0-.6.4-1 1-1h3.5c.6 0 1 .4 1 1 0 1.3.2 2.5.6 3.6.1.3 0 .7-.2 1z" fill="#1a8fd6"/></svg>
    (555) 014 2280
  </div>
  <nav class="main-nav">
    <a class="active" style="left:371px">Home</a>
    <a style="left:452px">About Us</a>
    <a style="left:560px">Our Services</a>
    <a style="left:694px">Why Us</a>
    <a style="left:790px">Blogs</a>
    <a style="left:869px">Our Work</a>
    <a style="left:979px">Contact Us</a>
  </nav>
</header>
<div class="brand-badge">
  <span class="brand-dot"></span>
  <span class="brand-name">BrightHaven Cleaning Services</span>
</div>

<section class="hero">
  <div class="hero-photo" role="img" aria-label="Yellow wheel loader clearing snow outside a building under a blue winter sky"></div>
  <svg class="hero-blob" width="490" height="330" viewBox="0 0 490 330">
    <path d="M40 250 C-10 190 10 90 120 45 C230 0 400 5 460 60 C510 110 470 210 380 270 C300 320 110 330 40 250Z" fill="#1e63c9" opacity=".82"/>
    <path d="M70 235 C30 180 60 100 150 68 C250 32 390 40 430 90 C460 135 420 215 340 250 C260 285 120 295 70 235Z" fill="#2a86e0" opacity=".55"/>
  </svg>
  <div class="hero-title">
    <h1>Indoor &amp; Outdoor</h1>
    <p>Cleaning Services</p>
  </div>
  <div class="btn-outline hero-call">Call Us Now</div>
  <span class="dot ring" style="left:1075px;top:219px"></span>
  <span class="dot" style="left:1075px;top:242px"></span>
  <span class="dot" style="left:1075px;top:265px"></span>
  <span class="dot" style="left:1075px;top:288px"></span>
  <span class="dot ring" style="left:554px;top:505px"></span>
  <span class="dot" style="left:578px;top:505px"></span>
  <span class="dot" style="left:602px;top:505px"></span>
  <span class="dot" style="left:626px;top:505px"></span>
  <svg class="hero-curve" width="1200" height="104" viewBox="0 0 1200 104">
    <path d="M0 104 C250 20 520 0 700 6 C900 12 1080 40 1200 70 L1200 104Z" fill="#fff"/>
  </svg>
</section>

<h2 class="section-title" style="top:700px">Our Services</h2>
<svg class="divider" style="top:747px" viewBox="0 0 346 24">
  <line x1="0" y1="12" x2="150" y2="12" stroke="#aaa" stroke-width="1"/>
  <line x1="196" y1="12" x2="346" y2="12" stroke="#aaa" stroke-width="1"/>
  <path d="M163 16 C160 6 174 2 180 8 M183 8 C186 18 172 22 166 16" fill="none" stroke="#4aa832" stroke-width="4" stroke-linecap="round"/>
</svg>

<div class="service-card" style="left:121px">
  <div class="service-photo" role="img" aria-label="Cleaner vacuuming beside a white sofa in a bright living room" style="background:linear-gradient(180deg,#eeeae4 0%,#d9d3cb 60%,#b98f6a 100%)"></div>
  <div class="service-label" style="background:#4aa832">Residential Cleaning</div>
</div>
<div class="service-card" style="left:448px">
  <div class="service-photo" role="img" aria-label="Pressure washer cleaning a paved path beside a green hedge" style="background:linear-gradient(180deg,#3d5a2c 0%,#6e7a5c 50%,#8a6e6a 100%)"></div>
  <div class="service-label" style="background:#2ba2df">Outdoor Cleaning</div>
</div>
<div class="service-card" style="left:775px">
  <div class="service-photo" role="img" aria-label="Office floor being mopped next to a yellow wet floor sign" style="background:linear-gradient(180deg,#dfe2e0 0%,#b7bcbb 55%,#7b8280 100%)"></div>
  <div class="service-label" style="background:#1b6b3a">Commercial Cleaning</div>
</div>

<section class="about">
  <div class="abs" role="img" aria-label="Person pushing a red lawn mower across a green lawn" style="left:0;top:0;width:760px;height:478px;background:linear-gradient(180deg,#9bbf6a 0%,#5e9b2a 45%,#3f7d19 100%)"></div>
  <svg class="about-panel" width="1200" height="478" viewBox="0 0 1200 478">
    <path d="M712 0 C640 80 620 300 740 478 L1200 478 L1200 0Z" fill="#0f6b32"/>
    <path d="M730 0 C660 80 644 300 764 478 L1200 478 L1200 0Z" fill="#4aa832"/>
  </svg>
  <div class="about-copy">
    <h2>About BrightHaven<br>Cleaning Services</h2>
    <p>Vivamus porttitor purus nisi eleifend libero a tempus libero lectus feugiat felis Morbi diam mauris</p>
    <p>Morbi porta Aibero id ullamcorper nonummy nibh ligula pulvinar metus eget consectetuer augue nisi quis lacus Ut ac mi quis lacus mollis eros</p>
  </div>
</section>
<div class="btn-outline about-more">Learn More</div>

<section class="work">
  <h2 class="section-title" style="top:50px">Recent Cleaning Work</h2>
  <svg class="divider" style="top:100px" viewBox="0 0 346 24">
    <line x1="0" y1="12" x2="150" y2="12" stroke="#aaa" stroke-width="1"/>
    <line x1="196" y1="12" x2="346" y2="12" stroke="#aaa" stroke-width="1"/>
    <path d="M163 16 C160 6 174 2 180 8 M183 8 C186 18 172 22 166 16" fill="none" stroke="#1b67c4" stroke-width="4" stroke-linecap="round"/>
  </svg>
  <div class="work-photo" role="img" aria-label="Pressure washing cobblestone paving" style="left:138px;background:linear-gradient(160deg,#8a8f8c,#3d4240)"></div>
  <div class="work-photo" role="img" aria-label="Vacuum cleaner on a carpet in warm light" style="left:356px;background:linear-gradient(160deg,#f3e6cf,#b9a48a)"></div>
  <div class="work-photo" role="img" aria-label="Man mowing the lawn in front of a house" style="left:586px;background:linear-gradient(180deg,#b9c7d6 0%,#7b6a5a 40%,#4d8a2c 100%)"></div>
  <div class="work-photo" role="img" aria-label="Cleaner wiping a white office desk" style="left:813px;background:linear-gradient(160deg,#f1f1ef,#c9d3cf)"></div>
  <svg class="abs" style="left:100px;top:1822px" width="0" height="0"></svg>
  <svg class="abs" style="left:100px;top:186px" width="36" height="70" viewBox="0 0 36 70"><path d="M34 2 L4 35 L34 68" fill="none" stroke="#1b67c4" stroke-width="4"/></svg>
  <svg class="abs" style="left:1064px;top:186px" width="36" height="70" viewBox="0 0 36 70"><path d="M2 2 L32 35 L2 68" fill="none" stroke="#1b67c4" stroke-width="4"/></svg>
</section>

<section class="why">
  <div class="why-photo" role="img" aria-label="Smiling cleaner in a green apron and yellow gloves tidying an office desk"></div>
  <div class="why-copy">
    <h2>Why Choose Us</h2>
    <p>We clean homes, apartments, condos, rental apt for people that are too busy or don't want to spend time cleaning when they can be doing other things.</p>
    <p>In addition, for businesses we offer cleaning services of offices, doctors/dentist offices, essentially any business. We are environmentally continuous and therefore use products that are not harmful to the environment, people or pets.</p>
  </div>
</section>
<div class="btn-solid">Learn More</div>

<footer class="site-footer">
  <div class="footer-brand">
    <span class="brand-dot"></span>
    <span class="brand-name">BrightHaven Cleaning Services</span>
  </div>
  <div class="footer-col" style="left:440px">
    <h3>QUICK LINKS</h3>
    <ul><li>Home</li><li>About Us</li><li>Why Us</li><li>Our Blogs</li></ul>
  </div>
  <div class="footer-col" style="left:636px">
    <h3>SERVICES</h3>
    <ul><li>Outdoor Cleaning</li><li>Residential Cleaning</li><li>Commercial Cleaning</li><li>Office Cleaning</li></ul>
  </div>
  <div class="footer-col" style="left:873px">
    <h3>CONTACT US</h3>
    <ul>
      <li class="contact-line"><svg width="16" height="20" viewBox="0 0 16 20" style="margin-top:5px"><path d="M8 1a6 6 0 0 0-6 6c0 4.5 6 12 6 12s6-7.5 6-12a6 6 0 0 0-6-6z" fill="none" stroke="#fff" stroke-width="1.6"/><circle cx="8" cy="7" r="2" fill="#fff"/></svg><span>48 Maple Row Suite 2<br>Austin 78701 TX</span></li>
      <li class="contact-line"><svg width="16" height="16" viewBox="0 0 24 24" style="margin-top:7px"><path d="M6.6 10.8a15.5 15.5 0 0 0 6.6 6.6l2.2-2.2c.3-.3.7-.4 1-.2 1.1.4 2.3.6 3.6.6.6 0 1 .4 1 1V20c0 .6-.4 1-1 1C10.6 21 3 13.4 3 4c0-.6.4-1 1-1h3.5c.6 0 1 .4 1 1 0 1.3.2 2.5.6 3.6.1.3 0 .7-.2 1z" fill="none" stroke="#fff" stroke-width="1.8"/></svg><span>555.019.4471</span></li>
      <li class="contact-line"><svg width="16" height="14" viewBox="0 0 16 14" style="margin-top:9px"><rect x="1" y="1" width="14" height="12" fill="none" stroke="#fff" stroke-width="1.4"/><path d="M1 1 L8 8 L15 1" fill="none" stroke="#fff" stroke-width="1.4"/></svg><span>hello@brighthaven.example</span></li>
    </ul>
  </div>
</footer>
<div class="copyright">© 2018 BrightHaven Cleaning Services &nbsp;All right reserved</div>

</body>
</html>
```